Income Tax Business Cards - Updates

Need to update these business cards while keeping all the same wording but just update them and make them look nicer and more modern/ on brand with our brand.

Industry/Entity Type

finance

Contact Information for Business Card

we have multiple locations so will just need to easily be able to change the address and phone numbers

Colors

Designer to choose colors to be used in the design.

```html
<!DOCTYPE html>
<html lang="en">
<head>
<meta charset="utf-8">
<title>Ledgerline Financial Group – Business Cards</title>
<link href="https://fonts.googleapis.com/css2?family=Anton&family=Montserrat:wght@500;600;700;800&display=swap" rel="stylesheet">
<style>
:root{
  --bg:#8a6a48;
  --green-dark:#0d4a26;
  --green:#1a6b38;
  --red:#c4202a;
  --red-light:#e23a3e;
  --white:#ffffff;
  --ink-green:#135a2e;
  --divider:#b9c4bb;
}
*{margin:0;padding:0;box-sizing:border-box}
html,body{width:900px;height:1200px;overflow:hidden}
body{background:var(--bg);font-family:"Montserrat",Arial,sans-serif;position:relative}
.card{position:absolute;left:68px;width:767px;height:450px;background:var(--white);overflow:hidden;box-shadow:0 6px 18px rgba(0,0,0,.45)}
.card--front{top:115px}
.card--back{top:636px}
.card svg.bands{position:absolute;left:0;top:0;width:767px;height:450px}
.abs{position:absolute;left:0;width:100%;text-align:center}
.headline{font-family:"Anton",Impact,sans-serif;color:transparent;
  background:linear-gradient(180deg,#ffffff 0%,#f4dede 45%,#d8353a 75%,#b5161f 100%);
  -webkit-background-clip:text;background-clip:text;
  filter:drop-shadow(0 3px 2px rgba(0,0,0,.35))}
.front-amount{top:18px;font-size:104px;line-height:1.1;letter-spacing:3px}
.subhead{color:var(--white);font-weight:700;letter-spacing:.5px}
.front-advance{top:130px;font-size:41px}
.front-note{top:181px;font-size:19px;font-weight:600;color:var(--white)}
.estimates{top:226px;font-size:29px;font-weight:800;color:var(--white);transform:rotate(-2deg)}
.phone{top:294px;display:flex;justify-content:center;align-items:center;gap:10px;
  font-family:"Anton",Impact,sans-serif;font-size:29px;color:var(--ink-green);letter-spacing:1.5px;padding-left:20px}
.phone-icon{width:30px;height:30px}
.contact-row{position:absolute;top:350px;left:0;width:100%;height:70px}
.brand-name{position:absolute;color:var(--ink-green);font-weight:700;text-align:center;line-height:1.15}
.front-brand{left:40px;top:8px;width:190px;font-size:22px}
.divider{position:absolute;top:10px;width:1px;height:55px;background:var(--divider)}
.contact-lines{position:absolute;left:258px;top:13px;font-size:17px;color:var(--ink-green);font-weight:500;line-height:24px}
.contact-lines div,.address{display:flex;align-items:center;gap:7px}
.icon-sm{width:15px;height:15px;flex:none}
.address{position:absolute;left:498px;top:4px;align-items:flex-start;font-size:16px;color:var(--ink-green);font-weight:500;line-height:21px}
.back-brand{left:0;width:100%;top:50px;font-size:30px}
.file-your{top:140px;font-size:58px;line-height:1.2;font-weight:700;color:var(--white)}
.back-taxes{top:210px;font-size:96px;line-height:1.1;letter-spacing:4px}
.back-amount{top:325px;display:flex;justify-content:center;align-items:center;gap:12px;
  font-family:"Anton",Impact,sans-serif;font-size:44px;color:var(--white);letter-spacing:1px}
.arrow{width:46px;height:22px}
.back-advance{top:378px;font-size:37px}
</style>
</head>
<body>

<section class="card card--front" aria-label="Business card front">
  <svg class="bands" viewBox="0 0 767 450" aria-hidden="true">
    <defs>
      <linearGradient id="greenFront" x1="0" y1="0" x2="0" y2="1">
        <stop offset="0" stop-color="#0b4424"/><stop offset="1" stop-color="#1f7a40"/>
      </linearGradient>
      <linearGradient id="redFront" x1="0" y1="0" x2="1" y2="0">
        <stop offset="0" stop-color="#b8141e"/><stop offset="1" stop-color="#e8424a"/>
      </linearGradient>
    </defs>
    <rect width="767" height="300" fill="url(#greenFront)"/>
    <path d="M0,255 Q383,178 767,238 L767,450 L0,450Z" fill="url(#redFront)"/>
    <path d="M0,330 Q383,240 767,305 L767,450 L0,450Z" fill="#ffffff"/>
    <path d="M160,450 Q383,405 610,450Z" fill="#c4202a"/>
  </svg>

  <div class="abs headline front-amount">UP TO $6,000</div>
  <div class="abs subhead front-advance">SAME DAY ADVANCE</div>
  <div class="abs front-note">NO APPROVED TAX RETURNS!</div>
  <div class="abs estimates">FREE ESTIMATES!</div>

  <div class="abs phone">
    <svg class="phone-icon" viewBox="0 0 30 30" aria-hidden="true">
      <circle cx="15" cy="15" r="15" fill="#c4202a"/>
      <path d="M10.5 8.5l2.5-.5 1.5 3.5-1.8 1.2a9 9 0 0 0 4.6 4.6l1.2-1.8 3.5 1.5-.5 2.5c-.3 1-1.3 1.5-2.3 1.3A12 12 0 0 1 9.2 10.8c-.2-1 .3-2 1.3-2.3z" fill="#fff"/>
    </svg>
    (023) 555-0148
  </div>

  <div class="contact-row">
    <div class="brand-name front-brand">Ledgerline<br>Financial Group</div>
    <span class="divider" style="left:238px"></span>
    <div class="contact-lines">
      <div><svg class="icon-sm" viewBox="0 0 16 16" aria-hidden="true"><rect x="1" y="3" width="14" height="10" fill="#c4202a"/><path d="M1 3l7 6 7-6" stroke="#fff" stroke-width="1.3" fill="none"/></svg>info@ledgerline.com</div>
      <div><svg class="icon-sm" viewBox="0 0 16 16" aria-hidden="true"><circle cx="8" cy="8" r="6.5" fill="none" stroke="#c4202a" stroke-width="1.6"/><ellipse cx="8" cy="8" rx="2.8" ry="6.5" fill="none" stroke="#c4202a" stroke-width="1.3"/><path d="M1.5 8h13" stroke="#c4202a" stroke-width="1.3"/></svg>www.ledgerline.com</div>
    </div>
    <span class="divider" style="left:480px"></span>
    <div class="address">
      <svg class="icon-sm" viewBox="0 0 16 16" aria-hidden="true" style="margin-top:3px"><path d="M8 1a5 5 0 0 0-5 5c0 4 5 9 5 9s5-5 5-9a5 5 0 0 0-5-5z" fill="#c4202a"/><circle cx="8" cy="6" r="2" fill="#fff"/></svg>
      <span>418 Harbor Street NW<br>Suite 210, Lakeview<br>MI 49000</span>
    </div>
  </div>
</section>

<section class="card card--back" aria-label="Business card back">
  <svg class="bands" viewBox="0 0 767 450" aria-hidden="true">
    <defs>
      <radialGradient id="greenBack" cx="0.5" cy="0.45" r="0.75">
        <stop offset="0" stop-color="#1d7a40"/><stop offset="1" stop-color="#0b4424"/>
      </radialGradient>
      <radialGradient id="redBack" cx="0.5" cy="1" r="0.8">
        <stop offset="0" stop-color="#e06a2a"/><stop offset="0.5" stop-color="#c72a28"/><stop offset="1" stop-color="#b8141e"/>
      </radialGradient>
    </defs>
    <rect width="767" height="450" fill="url(#greenBack)"/>
    <path d="M0,0 H767 V100 Q383,140 0,100Z" fill="#ffffff"/>
    <path d="M0,322 Q383,290 767,322 V450 H0Z" fill="url(#redBack)"/>
  </svg>

  <div class="brand-name back-brand">Ledgerline Financial Group</div>
  <div class="abs file-your subhead">FILE YOUR</div>
  <div class="abs headline back-taxes">TAXES HERE</div>
  <div class="abs back-amount">
    <svg class="arrow" viewBox="0 0 46 22" aria-hidden="true"><path d="M2 8h28V2l14 9-14 9v-6H2z" fill="none" stroke="#fff" stroke-width="2" stroke-linejoin="round"/></svg>
    UP TO $6,000
    <svg class="arrow" viewBox="0 0 46 22" aria-hidden="true"><path d="M44 8H16V2L2 11l14 9v-6h28z" fill="none" stroke="#fff" stroke-width="2" stroke-linejoin="round"/></svg>
  </div>
  <div class="abs subhead back-advance">SAME DAY ADVANCE</div>
</section>

</body>
</html>
```